Stationery Design Project

We need letterhead and business cards designed for our consulting firm. Color scheme, mostly deep blue (see logo). We are a commercial consulting work out firm, nationwide (large loans, $10MM and up). Visit our website for more info.
Updates

Project Deadline Extended
Reason: Meeting tomorrow morning to make final final decision. Would like this project to stay open to be able to provide feed back and receive final edits and approve. Thank you!!!

Target Market(s)

High end investors

Industry/Entity Type

Business

Requirements
Must have
• Letterhead must have the logo and the address

4719 Harlow Court, Suite 210, San Diego, CA 92108
Nice to have
• It would be nice to incorporate a watermark of all or some portion of the logo on the letterhead, or at least for the 2nd sheets.

Maybe our phone number: 858.555.0172
and/or webiste: www.tallpinecapital-example.com
Should not have
• Target users and audience of this will be men so, frilly or whimsical type designs are not preferred.

```html
<!DOCTYPE html>
<html lang="en">
<head>
<meta charset="utf-8">
<title>Tall Pine Capital – Business Card</title>
<link rel="stylesheet" href="https://fonts.googleapis.com/css2?family=Tinos:wght@400;700&display=swap">
<style>
  :root {
    --backdrop: #e9e7e3;
    --card: #ffffff;
    --brand-blue: #1e6bb0;
    --brand-blue-deep: #114f8c;
    --text-grey: #5a5a5a;
    --name-grey: #7b7b7b;
    --mark-grey: #c9c9c9;
    --rule-grey: #9a9a9a;
  }
  * { box-sizing: border-box; margin: 0; padding: 0; }
  html, body { width: 1200px; height: 900px; overflow: hidden; }
  body {
    background: var(--backdrop);
    font-family: "Tinos", "Times New Roman", serif;
    display: flex;
    align-items: center;
    justify-content: center;
    gap: 60px;
  }
  .card {
    position: relative;
    width: 525px;
    height: 300px;
    background: var(--card);
    box-shadow: 0 2px 10px rgba(0,0,0,0.12);
    overflow: hidden;
  }
  .band {
    position: absolute;
    left: 0;
    right: 0;
    height: 16px;
    background: linear-gradient(var(--brand-blue), var(--brand-blue-deep));
  }

  /* Front */
  .card-front .brand {
    position: absolute;
    top: 78px;
    left: 0;
    right: 0;
    display: flex;
    flex-direction: column;
    align-items: center;
    gap: 14px;
  }
  .card-front .brand-square {
    width: 44px;
    height: 44px;
    background: var(--name-grey);
  }
  .card-front .company {
    color: var(--name-grey);
    font-size: 44px;
    font-weight: 400;
    letter-spacing: 1px;
    line-height: 1;
  }
  .card-front .band { bottom: 38px; }

  /* Back */
  .card-back .band { top: 118px; width: 250px; right: auto; }
  .card-back .brand-faint {
    position: absolute;
    top: 30px;
    left: 18px;
    width: 240px;
    display: flex;
    align-items: center;
    gap: 10px;
  }
  .card-back .brand-faint .brand-square {
    width: 34px;
    height: 34px;
    background: var(--mark-grey);
    flex: none;
  }
  .card-back .brand-faint .company {
    color: var(--mark-grey);
    font-size: 27px;
    font-weight: 700;
    line-height: 1.05;
  }
  .contact {
    position: absolute;
    top: 34px;
    left: 276px;
    right: 18px;
    color: var(--text-grey);
    font-size: 14px;
    line-height: 1.35;
  }
  .contact .person {
    color: var(--brand-blue);
    font-weight: 700;
    font-size: 19px;
  }
  .contact .role { font-size: 16px; }
  .dotted-rule {
    border: 0;
    border-top: 2px dotted var(--rule-grey);
    margin: 14px 0;
  }
  .contact-line {
    display: flex;
    align-items: center;
    gap: 6px;
    white-space: nowrap;
  }
  .contact-line svg { width: 11px; height: 11px; fill: var(--text-grey); flex: none; }
</style>
</head>
<body>
  <section class="card card-front">
    <div class="brand">
      <div class="brand-square"></div>
      <h1 class="company">Tall Pine Capital</h1>
    </div>
    <div class="band"></div>
  </section>

  <section class="card card-back">
    <div class="brand-faint">
      <div class="brand-square"></div>
      <p class="company">Tall Pine Capital</p>
    </div>
    <div class="band"></div>
    <div class="contact">
      <p class="person">Daniel Reyes</p>
      <p class="role">Director</p>
      <hr class="dotted-rule">
      <p class="address">4719 Harlow Court, Suite 210,<br>San Diego, CA 92108</p>
      <hr class="dotted-rule">
      <p class="contact-line">
        <svg viewBox="0 0 24 24" aria-hidden="true"><path d="M6.6 10.8a15.1 15.1 0 0 0 6.6 6.6l2.2-2.2a1 1 0 0 1 1-.25 11.4 11.4 0 0 0 3.6.57 1 1 0 0 1 1 1V20a1 1 0 0 1-1 1A17 17 0 0 1 3 4a1 1 0 0 1 1-1h3.5a1 1 0 0 1 1 1c0 1.25.2 2.45.57 3.57a1 1 0 0 1-.25 1z"/></svg>
        858.555.0172
      </p>
      <p class="contact-line">
        <svg viewBox="0 0 24 24" aria-hidden="true"><circle cx="12" cy="12" r="10" fill="none" stroke="#5a5a5a" stroke-width="2.4"/><path d="M2 12h20M12 2c3 3 3 17 0 20M12 2c-3 3-3 17 0 20" fill="none" stroke="#5a5a5a" stroke-width="2"/></svg>
        www.tallpinecapital-example.com
      </p>
    </div>
  </section>
</body>
</html>
```